I want a double sided flyer possibly with a picture of a lawn or grass.
Company name, phone number, email, and logo
Halvorsen Turf Management, (404)726-1853,Halvorsen_Turf@brevimail.com
Company services
Fertilization and weed control,Lawn and Landscape maintenance, mowing, pruning, aeration, landscape and Christmas lights,

```html
<!DOCTYPE html>
<html lang="en">
<head>
<meta charset="utf-8">
<title>Halvorsen Turf Management – Services Flyer</title>
<link href="https://fonts.googleapis.com/css2?family=Arimo:wght@400;700&display=swap" rel="stylesheet">
<style>
  :root {
    --page-bg: #ececec;
    --sheet: #ffffff;
    --brand-green: #3aa343;
    --ink: #1e1e1e;
    --ink-soft: #3a3a3a;
    --info-panel: rgba(238, 236, 220, 0.88);
    --label-panel: rgba(255, 255, 255, 0.72);
    --grass-light: #8fbf4a;
    --grass-dark: #4f8a2a;
  }
  * { box-sizing: border-box; margin: 0; padding: 0; }
  html, body {
    width: 1200px; height: 1000px; overflow: hidden;
    background: var(--page-bg);
    font-family: "Arimo", Arial, sans-serif;
    color: var(--ink);
  }
  .flyer {
    position: absolute; left: 110px; top: 16px;
    width: 980px; height: 968px;
    background: var(--sheet);
  }
  .brand {
    position: absolute; left: 42px; top: 80px; width: 200px;
    display: flex; flex-direction: column; align-items: flex-start; gap: 12px;
  }
  .brand-dot {
    width: 62px; height: 62px; border-radius: 50%;
    background: var(--brand-green);
  }
  .brand-name {
    color: var(--brand-green); font-weight: 700;
    font-size: 22px; line-height: 1.15;
  }
  .contact-banner {
    position: absolute; left: 272px; top: 80px;
    width: 666px; height: 154px;
    background: linear-gradient(160deg, var(--grass-light) 0%, #6fa83a 45%, var(--grass-dark) 100%);
  }
  .contact-card {
    position: absolute; right: 0; top: 13px;
    width: 423px; height: 129px;
    background: var(--info-panel);
    padding: 18px 0 0 62px;
    font-size: 23px; line-height: 1.22; color: var(--ink);
  }
  .contact-card .label { font-weight: 700; }
  .contact-card .value { color: var(--ink-soft); }
  .service {
    position: absolute; top: 264px; width: 200px; height: 582px;
  }
  .service-photo { position: absolute; inset: 0; }
  .service-1 { left: 40px; }
  .service-2 { left: 272px; }
  .service-3 { left: 504px; }
  .service-4 { left: 736px; }
  .service-1 .service-photo {
    background: linear-gradient(180deg, #5f93c9 0%, #8fb2cf 14%, #2f5a2f 24%, #6f9a3d 45%, #5d922c 70%, #3f7422 100%);
  }
  .service-2 .service-photo {
    background: linear-gradient(180deg, #e4e8e6 0%, #9fb4aa 22%, #6b7d5a 40%, #6e9a3c 65%, #3f6d22 100%);
  }
  .service-3 .service-photo {
    background: linear-gradient(180deg, #b48ac2 0%, #c9a6d2 22%, #f1e6ee 48%, #d9c8dc 68%, #8a5fa2 88%, #3d2e46 100%);
  }
  .service-4 .service-photo {
    background: linear-gradient(180deg, #1b1b1b 0%, #4a4a4a 10%, #e9e9e9 18%, #dcdcdc 55%, #2a2a2a 64%, #121212 100%);
  }
  .service-label {
    position: absolute; left: 19px;
    background: var(--label-panel);
    padding: 10px 12px;
    font-size: 16px; line-height: 1.2; color: var(--ink);
  }
  .service-1 .service-label { top: 272px; width: 181px; }
  .service-2 .service-label { top: 368px; left: 2px; width: 182px; }
  .service-3 .service-label { top: 484px; width: 181px; }
  .service-4 .service-label { top: 419px; width: 163px; }
</style>
</head>
<body>
  <main class="flyer">
    <div class="brand">
      <div class="brand-dot"></div>
      <div class="brand-name">Halvorsen<br>Turf Management</div>
    </div>

    <section class="contact-banner" role="img" aria-label="Close-up photo of a freshly mown green lawn">
      <div class="contact-card">
        <div class="label">Halvorsen Turf Management</div>
        <div><span class="label">phone:</span> <span class="value">(404)726-1853</span></div>
        <div><span class="label">mail:</span> <span class="value">Halvorsen_Turf@brevimail.com</span></div>
      </div>
    </section>

    <section class="service service-1">
      <div class="service-photo" role="img" aria-label="Tall grass blades in a meadow with pine trees and blue sky"></div>
      <p class="service-label">Fertilization<br>and weed control</p>
    </section>

    <section class="service service-2">
      <div class="service-photo" role="img" aria-label="Succulent plant above green grass"></div>
      <p class="service-label">Lawn and landscape<br>maintenance</p>
    </section>

    <section class="service service-3">
      <div class="service-photo" role="img" aria-label="Pink and white blossoms on a dark branch"></div>
      <p class="service-label">Pruning, mowing,<br>aeration</p>
    </section>

    <section class="service service-4">
      <div class="service-photo" role="img" aria-label="White paper lantern hanging against a dark background"></div>
      <p class="service-label">Landscape and<br>Christmas lights</p>
    </section>
  </main>
</body>
</html>
```